Menu Design Project

Recreate the menu front and back AS CLOSE AS POSSIBLE! Colors matching is important. Categories need to correspond with these pages:

Pages are numbered 1-6 1-3 being left to right when menu open 4 back of 1, 5 back of 2, and 6 is back of 3.

page 1 = starters (include flatbreads under this section),
soups & salads

Page 2 = Wings (marlo holding wings art)
Burgers
Burger toppings

Page 3 = Sandwiches and wraps
entrees

Page 4 = Logo (this will be the front page when folded)
hours of operation
phone #
address
email
Facebook or website URL

Page 5 = Lunch specials mon - fri 11am - 4pm
HH menu and times 4-7 mon - fri 10pm - close daily
Raw consumption quote
18% gratuity added to parties of 8 or more

Page 6 = Desserts
Soft drinks
Draft/bottle beers
$5 glass of wine Cab, Pinot Noir, White Zyn, Chardonnay

We cant get the high res files so we are having to recreate the menu.

Need small changes to menu content as well.

Please see attached files for current menu.

• **Front Side of menu***

MARLO’S JUMBO WINGS

Served with House or Blue Cheese Dressing and Celery

GRILLED OR FRIED

5 pieces ..............................................................................5.45
10 pieces.............................................................................10.45
25 pieces...........................................................................23.95
50 pieces...........................................................................44.95

MARLO’S HOMEMADE SAUCES

Marlo's Wing Sauce
Mild
Medium
Hot
Inferno
Honey Garlic
BBQ
Spicy Mango BBQ
Mango Habenero
Cajun
Jamaican Jerk
Rasberry
Spicy Rasberry
Pineapple Teriyaki
Lemon Pepper
Honey Glazed
Guava Tequila Lime
Garlic Parmesan
Honey Mustard

MARLO’S APPETIZERS

One Dozen Steamers ...............................................8.45
Jalapeńo Crab Nuggets ...........................................6.95
Buffalo Chicken Tenders..........................................6.95
Waffle Fries ..............................................................4.95
Sweet Potato Fries ...................................................5.95
Honey Glazed Sweet Potato Fries...........................6.95
Onion Rings..............................................................5.95
Coconut Shrimp .......................................................7.95
Buffalo Shrimp.............................................................7.95
Mozzarella Sticks...................................................6.45

MARLO’S JUICY HALF POUND HOMEMADE BURGERS

All Burgers Served with Crispy Waffle Fries

CHEESEBURGER

Your Choice of American, Swiss, Provolone or
Cheddar Cheese with Sliced Tomato, Red Onion
and Iceberg Lettuce .......................................8.95

BBQ BURGER

Brushed with Barbecue Sauce and Piled High
with Melted Cheddar Cheese, Crispy Onion
Rings,
Sliced Tomato and Iceberg Lettuce ...............9.25

CAJUN BURGER

Dusted with Cajun Seasoning then Covered
with Blue Cheese Crumbles, Crunchy Bacon,
Iceberg Lettuce, Sliced Tomato, Red Onion and
Ranch Dressing ...............................................9.25

TOPPINGS AND EXTRAS .50 EACH

Blue Cheese Crumbles, Sautéed Mushrooms, Sautéed
Onions, Crunchy Bacon, Blue Cheese Dressing,
House Dressing, Onion Rings, BBQ Sauce, Cajun
Seasoning, Dunmore Seasoning, Red Onion,
Sliced Tomato, Chili, Mango and Jalapeńo Salsa

THE “GIANT MARLO BURGER”.................13.95

One Pound of Fresh Ground Beef
Served with Iceberg Lettuce,
Sliced Tomato, Red Onion,

2847 NORTH HARBIN CREST, WEST PALM BEACH, FLORIDA 33415

561-555-0193 • MARLOSGRILLHUT.EXAMPLE

WARNING: CONSUMPTION OF RAW OR UNDERCOOKED MEAT, SEAFOOD OR POULTRY MAY INCREASE THE RISK OF FOOD-BOURNE ILLNESSES.
ASK YOUR SERVER IF YOU HAVE SPECIFIC DIETARY REQUIREMENTS.

Happy Hour Menu
1/4 lb Hamburger..............2.95
1/4 lb Cheeseburger.................3.45
Hot Dog....................1.95
Mozzarella Sticks........................3.45
Steamed Little Neck Clams........4.95

Lunch Specials............6.45
6 Wings and Fries
Chicken Caesar Salad
Buffalo Chicken Wrap and fries
1/4 lb Hot Dog and fries
Hamburger and fries
Cheeseburger and fries

Domestic Draft..............3.00 Regular 2.50 Happy Hour Pitcher 8.95
Fenner Pale
Glendorfer
Glen Pale
Harlan's Pale

Imported Draft..........3.50 Regular 3.00 Happy Hour Pitcher 9.95
Vostrand
Crag Peak

Domestic Bottles.............3.50 Regular 2.25 Happy Hour
Glendorfer
Glen Pale
Glen Pale Citra
Harlan's Pale
Fenner Pale
Pelstrom Extra

Import Bottles...............4.00
Lumera
Lumera Pale
Brovaard
Brovaard Pale
Sandor
Oscuro Sandor
Tres Halcones
Sulon
Varkov Chill
Ned Porter's
Fennick's

Buckets
Domestic Bucket of 5 12.00
Import Bucket of 5 15.00

WINE............................5.50 4.50 Happy Hour
Cabernet
Merlot
Chardonny
White Zinfendel

**Back Menu Side**

SANDWICHES 1 Side

CRISPY CHICKEN BLT
A Lightly Breaded, Crispy Fried, Fresh Chicken Breast with
Crunchy Bacon, Melted Provolone Cheese, Sliced Tomato,
Iceberg Lettuce and Creamy Ranch Dressing .................8.75

MANGO BBQ GRILLED CHICKEN SANDWICH
A Fresh Chicken Breast Grilled to Perfection and Drizzled with
our House Made Mango BBQ Sauce Piled High with Crispy
Onion Rings, Sliced Tomato and Iceberg Lettuce..............8.75

JAMAICAN JERKED MAHI SANDWICH
Juicy Pieces of Sauteed Mahi Rubbed with Jamaican Jerk
Seasoning and Topped with Spicy Mayonnaise,
Iceberg Lettuce, Sliced Tomato and Red Onion .............9.45

BROILED OR BLACKENED FISH SANDWICH.........................8.75
Broiled or Balckened white fish with lettuce and tomato, served with
tartar sauce.
All Sandwiches and Wraps Served with Crispy Waffle Fries

BUFFALO CHICKEN SUB
Buffalo chicken tossed in your choice of sauce with blue cheese dressing. Topped
with lettuce and tomato on a toasted sub roll.................8.75

CHICKEN PARMESAN SUB
Fried chicken tenders topped with provolone cheese and maranara sauce
on a toasted sub roll...................................................8.75

MARLO’S GIANT 1/4LB ALL BEEF HOT DOG...........................6.95 1 Side
SALADS

BUFFALO CHICKEN SALAD
Plain, Mild, Hot or Extra Hot Crispy Chicken Tenders
Covered with Blue Cheese Crumbles and Ranch Dressing
Served over Romaine Lettuce with Cucumbers, Celery,
Diced Tomato and Scallions .............................................8.95

CLASSIC WEDGE
A Wedge of Iceberg Lettuce Topped with
House Blue Cheese Dressing and Diced Tomato ............5.95

CAESAR SALAD
Marlo’s Homemade Version of the Classic......................4.95

TOSSED SALAD
Romaine Lettuce, Cucumbers, Diced Tomatoes, and
Red Onion Tossed in Ranch Dressing ..............................4.95

ADD ONS
Grilled Chicken .................................................................3.95
Sauteed Mahi....................................................................4.95
Grilled Shrimp...................................................................4.95
Crispy Chicken Tenders.....................................................3.95
Crunchy Bacon ................................................................... .95

SIDES
Waffle Fries .....................................................2.25
Sweet Potato Fries..........................................2.95
Honey Glazed Sweet Potato Fries .................3.65
Onion rings .....................................................2.25
Cole Slaw.........................................................2.25
Black Beans and Rice....................................................2.25
Corn on the Cob .............................................. 2.25
Baked Potato...............................................2.25
Mixed Vegetables..................................................2.25

Soups Cup......3.50 Bowl.........5.50
Soup of the Day
Chili

FLATBREADS
BBQ Chicken.....................................7.95
Buffalo Chicken........................7.95

DRINKS
Zolta........................2.45
Diet Zolta ...............2.45
Vale Breeze.............2.45
Orange Whirl ......................2.45
Canyon Fizz ..........2.45
Lemonade .............2.45
Sweet or Unsweetened Tea ..............2.45
APPLE JUICE.............2.45
ORANGE JUICE ........2.45
CRANBERRY JUICE ..2.45
BOTTLED WATER.....2.45
HOT TEA ..................2.45
COFFEE.....................2.45
ALL KIDS DRINKS ARE
SERVED WITH A CUP
AND LID FOR ..............99

DESSERT
Key Lime Pie...................................4.95
Choclate Layered Cake....................4.95
NY Style Cheesecake.........................................4.95
Warm Apple Cobbler................................................4.95
Pruett's Pie..........................................4.95

MARLO’S DINNERS 2 Side
GRILLED MAHI
Fresh Grilled Mahi, with Your Choice of Any Sauce....14.95
GRILLED or FRIED SHRIMP
Juicy Shrimp Hot Off the Grill, with Your Choice
of any Sauce...................................................................13.95
BROILED or BLACKENED FISH
Tender White Fish Brioled or Blackened and Served with Tartar Sauce................13.95
MARINATED PORK TENDERLOIN
Two Tender Pork Medallions Marinated and served with two sides..............................11.95

WRAPS 1 Side
BUFFALO CHICKEN WRAP
Your choice of mild, hot, or extra hot Crispy Chicken Tenders
with Red Onion, Sliced Tomato, Iceberg Lettuce, Blue Cheese
Crumbles and Ranch Dressing in a Flour Tortilla..............8.75
SOUTHWEST CHICKEN WRAP
Grilled chicken with black beans, rice, sour cream, salsa,cheddar
and jack cheese, with our spicy southwest sauce....................8.75
CHICKEN CAESAR WRAP
Fresh Sliced Grilled Chicken Breast in a Flour Tortilla
with Romaine Lettuce and Caesar Dressing ...................8.75
KEY WEST WRAP
Grilled Chicken tossed in mango habanero souce, Lettuce, Tomato, Onion, and
spicy mayo................................................................8.75
CAJUN SHRIMP WRAP
Tender Shrimp Dusted with Cajun Seasoning in a
Flour Tortilla, lettuce, tomatoe, and onion .....9.45

KIDS MENU........5.95 1 Side
Hamburger
Cheeseburger
Hot Dog
Grilled Cheese
Mac n' Cheese
Chicken Tenders

```html
<!DOCTYPE html>
<html lang="en">
<head>
<meta charset="utf-8">
<title>Marlo's Menu – Inside Spread</title>
<link rel="stylesheet" href="https://fonts.googleapis.com/css2?family=Permanent+Marker&family=Patrick+Hand+SC&display=swap">
<style>
  :root{
    --sky-top:#f8dd93;
    --sky-mid:#f5cf72;
    --sky-low:#eebd55;
    --heading:#d9501c;
    --heading-edge:#3a1806;
    --ink:#24160a;
    --board:#6b421c;
    --board-text:#fbe8bf;
    --figure:#d98a3a;
    --figure-low:#8a5526;
  }
  *{box-sizing:border-box;margin:0;padding:0}
  html,body{width:1200px;height:737px;overflow:hidden}
  body{font-family:"Patrick Hand SC",cursive;color:var(--ink)}
  .menu-spread{position:relative;width:1200px;height:737px;overflow:hidden}
  .beach-scene{position:absolute;inset:0;
    background:
      radial-gradient(ellipse 260px 140px at 300px 440px,rgba(255,245,200,.55),transparent 70%),
      linear-gradient(180deg,var(--sky-top) 0%,var(--sky-mid) 55%,var(--sky-low) 100%)}
  .column{position:absolute;top:0;height:737px}
  .col-left{left:52px;width:350px}
  .col-mid{left:432px;width:330px}
  .col-right{left:822px;width:330px}
  .section{position:absolute;left:0;right:0}
  .section-title{font-family:"Permanent Marker",cursive;color:var(--heading);font-size:22px;text-align:center;letter-spacing:.5px;line-height:26px;
    text-shadow:1px 1px 0 var(--heading-edge),-1px 1px 0 var(--heading-edge),1px -1px 0 var(--heading-edge),-1px -1px 0 var(--heading-edge)}
  .section-note{text-align:center;font-size:10px;line-height:13px;margin-bottom:4px}
  .sub-title{font-family:"Permanent Marker",cursive;font-size:12px;line-height:15px;letter-spacing:.4px}
  .item{margin-bottom:7px}
  .line{display:flex;align-items:baseline;font-size:11px;line-height:13px}
  .item-name{font-family:"Permanent Marker",cursive;font-size:11px;letter-spacing:.4px;white-space:nowrap}
  .leader{flex:1;border-bottom:1.5px dotted var(--ink);margin:0 2px;transform:translateY(-3px)}
  .price{white-space:nowrap;font-size:11px}
  .desc{font-size:11px;line-height:13px}
  .list .line{margin-bottom:1px}
  .list .line span:first-child{white-space:nowrap}
  .kids-list{font-size:11px;line-height:14px}
  .hotdog-board{position:absolute;left:0;top:644px;width:350px;height:64px;background:var(--board);color:var(--board-text);
    font-family:"Permanent Marker",cursive;text-align:center;font-size:16px;line-height:24px;padding-top:8px;letter-spacing:.6px}
  .mascot-art{position:absolute;left:573px;top:445px;width:190px;height:292px;border-radius:60px 60px 0 0;
    background:linear-gradient(180deg,var(--figure) 0%,var(--figure-low) 100%)}
  .drinks-grid{display:flex;gap:14px}
  .drinks-grid .list{flex:1}
  .soups .line{font-size:11px}
</style>
</head>
<body>
<main class="menu-spread">
  <div class="beach-scene" role="img" aria-label="Sunset beach scene with palm tree silhouettes"></div>

  <!-- Left column: sandwiches and wraps -->
  <section class="column col-left">
    <div class="section" style="top:18px">
      <h2 class="section-title">Sandwiches</h2>
      <p class="section-note">All sandwiches and wraps served with crispy waffle fries</p>
      <div class="item"><div class="line"><span class="item-name">Crispy Chicken BLT</span><span class="leader"></span><span class="price">8.75</span></div>
        <p class="desc">A lightly breaded, crispy fried, fresh chicken breast with crunchy bacon, melted provolone cheese, sliced tomato, iceberg lettuce and creamy ranch dressing</p></div>
      <div class="item"><div class="line"><span class="item-name">Mango BBQ Grilled Chicken Sandwich</span><span class="leader"></span><span class="price">8.75</span></div>
        <p class="desc">A fresh chicken breast grilled to perfection and drizzled with our house made mango BBQ sauce piled high with crispy onion rings, sliced tomato and iceberg lettuce</p></div>
      <div class="item"><div class="line"><span class="item-name">Jamaican Jerked Mahi Sandwich</span><span class="leader"></span><span class="price">9.45</span></div>
        <p class="desc">Juicy pieces of sauteed mahi rubbed with Jamaican jerk seasoning and topped with spicy mayonnaise, iceberg lettuce, sliced tomato and red onion</p></div>
      <div class="item"><div class="line"><span class="item-name">Broiled or Blackened Fish Sandwich</span><span class="leader"></span><span class="price">8.75</span></div>
        <p class="desc">Broiled or blackened white fish with lettuce and tomato, served with tartar sauce.</p></div>
    </div>

    <div class="section" style="top:322px">
      <h2 class="section-title">Wraps</h2>
      <div class="item"><div class="line"><span class="item-name">Buffalo Chicken Wrap</span><span class="leader"></span><span class="price">8.75</span></div>
        <p class="desc">Your choice of mild, hot, or extra hot crispy chicken tenders with red onion, sliced tomato, iceberg lettuce, blue cheese crumbles and ranch dressing in a flour tortilla</p></div>
      <div class="item"><div class="line"><span class="item-name">Southwest Chicken Wrap</span><span class="leader"></span><span class="price">8.75</span></div>
        <p class="desc">Grilled chicken with black beans, rice, sour cream, salsa, cheddar and jack cheese, with our spicy southwest sauce</p></div>
      <div class="item"><div class="line"><span class="item-name">Chicken Caesar Wrap</span><span class="leader"></span><span class="price">8.75</span></div>
        <p class="desc">Fresh sliced grilled chicken breast in a flour tortilla with romaine lettuce and caesar dressing</p></div>
      <div class="item"><div class="line"><span class="item-name">Key West Wrap</span><span class="leader"></span><span class="price">8.75</span></div>
        <p class="desc">Grilled chicken tossed in mango habanero sauce, lettuce, tomato, onion, and spicy mayo</p></div>
      <div class="item"><div class="line"><span class="item-name">Cajun Shrimp Wrap</span><span class="leader"></span><span class="price">9.45</span></div>
        <p class="desc">Tender shrimp dusted with cajun seasoning in a flour tortilla, lettuce, tomato, and onion</p></div>
    </div>

    <div class="hotdog-board">Marlo's Giant 1/4lb<br>All-Beef Hot Dog..........6.95</div>
  </section>

  <!-- Middle column: dinners, salads, add ons, kids -->
  <section class="column col-mid">
    <div class="section" style="top:18px">
      <h2 class="section-title">Marlo's Dinners</h2>
      <div class="item"><div class="line"><span class="item-name">Grilled Mahi</span><span class="leader"></span><span class="price">14.95</span></div>
        <p class="desc">Fresh grilled mahi, with your choice of any sauce</p></div>
      <div class="item"><div class="line"><span class="item-name">Grilled or Fried Shrimp</span><span class="leader"></span><span class="price">13.95</span></div>
        <p class="desc">Juicy shrimp hot off the grill, with your choice of any sauce</p></div>
      <div class="item"><div class="line"><span class="item-name">Broiled or Blackened Fish</span><span class="leader"></span><span class="price">13.95</span></div>
        <p class="desc">Tender white fish broiled or blackened and served with tartar sauce</p></div>
      <div class="item"><div class="line"><span class="item-name">Marinated Pork Tenderloin</span><span class="leader"></span><span class="price">11.95</span></div>
        <p class="desc">Two tender pork medallions marinated and served with two sides</p></div>
    </div>

    <div class="section" style="top:208px">
      <h2 class="section-title">Salads</h2>
      <div class="item"><div class="line"><span class="item-name">Buffalo Chicken Salad</span><span class="leader"></span><span class="price">8.95</span></div>
        <p class="desc">Plain, mild, hot or extra hot crispy chicken tenders covered with blue cheese crumbles and ranch dressing served over romaine lettuce with cucumbers, celery, diced tomato and scallions</p></div>
      <div class="item"><div class="line"><span class="item-name">Classic Wedge</span><span class="leader"></span><span class="price">5.95</span></div>
        <p class="desc">A wedge of iceberg lettuce topped with house blue cheese dressing and diced tomato</p></div>
      <div class="item"><div class="line"><span class="item-name">Caesar Salad</span><span class="leader"></span><span class="price">4.95</span></div>
        <p class="desc">Marlo's homemade version of the classic</p></div>
      <div class="item"><div class="line"><span class="item-name">Tossed Salad</span><span class="leader"></span><span class="price">4.95</span></div>
        <p class="desc">Romaine lettuce, cucumbers, diced tomatoes, and red onion tossed in ranch dressing</p></div>
    </div>

    <div class="section list" style="top:452px;width:142px">
      <h3 class="sub-title">Add Ons</h3>
      <div class="line"><span>Grilled Chicken</span><span class="leader"></span><span class="price">3.95</span></div>
      <div class="line"><span>Sauteed Mahi</span><span class="leader"></span><span class="price">4.95</span></div>
      <div class="line"><span>Grilled Shrimp</span><span class="leader"></span><span class="price">4.95</span></div>
      <div class="line"><span>Crispy Chicken Tenders</span><span class="leader"></span><span class="price">3.95</span></div>
      <div class="line"><span>Crunchy Bacon</span><span class="leader"></span><span class="price">0.95</span></div>
    </div>

    <div class="section" style="top:570px;width:142px">
      <div class="line"><span class="sub-title">Kid's Menu</span><span class="leader"></span><span class="price">5.95</span></div>
      <p class="kids-list">Hamburger<br>Cheeseburger<br>Hot Dog<br>Grilled Cheese<br>Mac n' Cheese<br>Chicken Tenders</p>
    </div>
  </section>

  <div class="mascot-art" role="img" aria-label="Mascot illustration in a sun hat and beach shirt holding a drink beside a surfboard"></div>

  <!-- Right column: subs, sides, soups, flatbreads, drinks, dessert -->
  <section class="column col-right">
    <div class="section" style="top:18px">
      <h2 class="section-title">Subs</h2>
      <div class="item"><div class="line"><span class="item-name">Buffalo Chicken Sub</span><span class="leader"></span><span class="price">8.75</span></div>
        <p class="desc">Buffalo chicken tossed in your choice of sauce with blue cheese dressing. Topped with lettuce and tomato on a toasted sub roll</p></div>
      <div class="item"><div class="line"><span class="item-name">Chicken Parmesan Sub</span><span class="leader"></span><span class="price">8.75</span></div>
        <p class="desc">Fried chicken tenders topped with provolone cheese and marinara sauce on a toasted sub roll</p></div>
    </div>

    <div class="section list" style="top:154px">
      <h3 class="sub-title">Sides</h3>
      <div class="line"><span>Waffle Fries</span><span class="leader"></span><span class="price">2.25</span></div>
      <div class="line"><span>Sweet Potato Fries</span><span class="leader"></span><span class="price">2.95</span></div>
      <div class="line"><span>Honey Glazed Sweet Potato Fries</span><span class="leader"></span><span class="price">3.65</span></div>
      <div class="line"><span>Onion Rings</span><span class="leader"></span><span class="price">2.25</span></div>
      <div class="line"><span>Cole Slaw</span><span class="leader"></span><span class="price">2.25</span></div>
      <div class="line"><span>Black Beans and Rice</span><span class="leader"></span><span class="price">2.25</span></div>
      <div class="line"><span>Corn on the Cob</span><span class="leader"></span><span class="price">2.25</span></div>
      <div class="line"><span>Baked Potato</span><span class="leader"></span><span class="price">2.25</span></div>
      <div class="line"><span>Mixed Vegetables</span><span class="leader"></span><span class="price">2.25</span></div>
    </div>

    <div class="section soups" style="top:328px">
      <h3 class="sub-title">Soups</h3>
      <div class="line" style="width:210px"><span>Cup</span><span class="leader"></span><span class="price">3.50 Bowl</span><span class="leader"></span><span class="price">5.50</span></div>
      <p class="desc">Soup of the Day: Chili</p>
    </div>

    <div class="section list" style="top:394px">
      <h3 class="sub-title">Flatbreads</h3>
      <div class="line"><span>BBQ Chicken</span><span class="leader"></span><span class="price">7.95</span></div>
      <div class="line"><span>Buffalo Chicken</span><span class="leader"></span><span class="price">7.95</span></div>
    </div>

    <div class="section" style="top:468px">
      <h3 class="sub-title">Drinks</h3>
      <div class="drinks-grid">
        <div class="list">
          <div class="line"><span>Zolta</span><span class="leader"></span><span class="price">2.45</span></div>
          <div class="line"><span>Diet Zolta</span><span class="leader"></span><span class="price">2.45</span></div>
          <div class="line"><span>Vale Breeze</span><span class="leader"></span><span class="price">2.45</span></div>
          <div class="line"><span>Orange Whirl</span><span class="leader"></span><span class="price">2.45</span></div>
          <div class="line"><span>Canyon Fizz</span><span class="leader"></span><span class="price">2.45</span></div>
          <div class="line"><span>Lemonade</span><span class="leader"></span><span class="price">2.45</span></div>
          <div class="line"><span>Sweet or Unsweetened Tea</span><span class="leader"></span><span class="price">2.45</span></div>
        </div>
        <div class="list">
          <div class="line"><span>Apple Juice</span><span class="leader"></span><span class="price">2.45</span></div>
          <div class="line"><span>Orange Juice</span><span class="leader"></span><span class="price">2.45</span></div>
          <div class="line"><span>Cranberry Juice</span><span class="leader"></span><span class="price">2.45</span></div>
          <div class="line"><span>Bottled Water</span><span class="leader"></span><span class="price">2.45</span></div>
          <div class="line"><span>Hot Tea</span><span class="leader"></span><span class="price">2.45</span></div>
          <div class="line"><span>Coffee</span><span class="leader"></span><span class="price">2.45</span></div>
          <p class="desc" style="font-size:10px">All kids drinks are served with</p>
          <div class="line" style="font-size:10px"><span>a cup and lid for</span><span class="leader"></span><span class="price">0.99</span></div>
        </div>
      </div>
    </div>

    <div class="section list" style="top:594px">
      <h3 class="sub-title">Dessert</h3>
      <div class="line"><span>Key Lime Pie</span><span class="leader"></span><span class="price">4.95</span></div>
      <div class="line"><span>Chocolate Layered Cake</span><span class="leader"></span><span class="price">4.95</span></div>
      <div class="line"><span>NY Style Cheesecake</span><span class="leader"></span><span class="price">4.95</span></div>
      <div class="line"><span>Warm Apple Cobbler</span><span class="leader"></span><span class="price">4.95</span></div>
      <div class="line"><span>Pruett's Pie</span><span class="leader"></span><span class="price">4.95</span></div>
    </div>
  </section>
</main>
</body>
</html>
```